TIME BAR Design Project

DESIGN: TIME LAPSE BAR

We are looking for a fresh design for a time lapse bar which would appear on screen during an exercise video.

Please see a quick example attached. We would like it to be created in Photoshop or Illustrator, in layers. ( no after effects please).

We need a layer that would move to indicate the time passing.

We would like to manipulate the time as needed for various pieces.
Updates

Quick update:
please note the current bar in the sample picts was done in-house and is only intended to be a guide.  The bar does not have to resemble the sample. Thanks.

Target Market(s)

male /female 25-65 60% women.

Requirements
Must have
• Created in Photoshop or Illustrator.

Minimum 300DPI.

Please see that there is needs to be a place for the name of each exercise - this can appear and then fade out.
Nice to have
• -bar should match the mood of the set and colors.( see picts).

-bar CAN BE see-through so that the body's are seen behind it.
Should not have
• too high tech or masculine

too feminine

```html
<!DOCTYPE html>
<html lang="en">
<head>
<meta charset="utf-8">
<title>Time Lapse Bar</title>
<link rel="stylesheet" href="https://fonts.googleapis.com/css2?family=Open+Sans:wght@400;600&display=swap">
<style>
  :root {
    --wall-light: #f3efe8;
    --wall-warm: #e9d9c2;
    --pillar-orange: #d98a2e;
    --floor-light: #d8b27e;
    --floor-deep: #b4834c;
    --silver-top: rgba(236, 238, 240, 0.92);
    --silver-bottom: rgba(170, 174, 180, 0.92);
    --graphite-top: rgba(70, 72, 76, 0.94);
    --graphite-bottom: rgba(36, 37, 40, 0.94);
    --progress-top: #f4a13c;
    --progress-mid: #ec7a22;
    --progress-edge: #d8321c;
    --track-light: rgba(250, 240, 225, 0.85);
    --track-dark: rgba(60, 58, 56, 0.9);
  }
  * { margin: 0; padding: 0; box-sizing: border-box; }
  html, body {
    width: 1200px;
    height: 900px;
    overflow: hidden;
    font-family: "Open Sans", sans-serif;
  }
  .video-frame {
    position: relative;
    width: 1200px;
    height: 900px;
    overflow: hidden;
  }
  .studio-scene {
    position: absolute;
    inset: 0;
    background:
      linear-gradient(90deg, transparent 0 770px, rgba(217,138,46,0.55) 770px 830px, transparent 830px 1050px, rgba(217,138,46,0.55) 1050px 1100px, transparent 1100px),
      linear-gradient(180deg, var(--wall-light) 0%, var(--wall-warm) 50%, var(--floor-light) 56%, var(--floor-deep) 100%);
  }
  .time-bar {
    position: absolute;
    left: 120px;
    width: 956px;
    height: 72px;
    border-radius: 3px;
  }
  .time-bar--light {
    top: 632px;
    background: linear-gradient(180deg, var(--silver-top), var(--silver-bottom));
    box-shadow: 0 2px 6px rgba(0,0,0,0.25), inset 0 1px 0 rgba(255,255,255,0.8);
  }
  .time-bar--dark {
    top: 786px;
    height: 70px;
    background: linear-gradient(180deg, var(--graphite-top), var(--graphite-bottom));
    box-shadow: 0 2px 6px rgba(0,0,0,0.35), inset 0 1px 0 rgba(255,255,255,0.15);
  }
  .time-track {
    position: absolute;
    left: 16px;
    top: 16px;
    width: 672px;
    height: 40px;
    overflow: hidden;
  }
  .time-bar--light .time-track { background: var(--track-light); }
  .time-bar--dark .time-track {
    top: 16px;
    height: 36px;
    background: var(--track-dark);
    border: 1px solid rgba(255,255,255,0.12);
  }
  .time-progress {
    position: absolute;
    left: 0;
    top: 0;
    bottom: 0;
    width: 364px;
    background: linear-gradient(180deg, var(--progress-top) 0%, var(--progress-mid) 60%, var(--progress-edge) 100%);
    border-bottom: 6px solid var(--progress-edge);
  }
</style>
</head>
<body>
  <main class="video-frame">
    <div class="studio-scene" role="img" aria-label="Exercise video still: two instructors swinging a flexible bar in a bright studio with orange pillars and a wooden floor"></div>

    <div class="time-bar time-bar--light">
      <div class="time-track">
        <div class="time-progress"></div>
      </div>
    </div>

    <div class="time-bar time-bar--dark">
      <div class="time-track">
        <div class="time-progress"></div>
      </div>
    </div>
  </main>
</body>
</html>
```